Harmony Swift Care Business card

We want a business card that matches our business theme. Our website is www.swiftcarehub.example
The company name is Harmony Swift Care
The persons having the business cards will be doctors
My logo is attached.
We have a drive-thru medical center where our motto is Fast, Reliable, and Convenient. Our goal is to change the medical space while utilizing technologies, keeping a professional and clean look

Medical

Info on the card should be: Name, Position, Cell number, website, email address, possibly the office line as well

Requirements
Must have
• Logo
Nice to have
• Professional medical feel with our logo colors incorporated

```html
<!DOCTYPE html>
<html lang="en">
<head>
<meta charset="utf-8">
<title>Harmony Swift Care – Business Card</title>
<link rel="stylesheet" href="https://fonts.googleapis.com/css2?family=Arimo:wght@400;700&family=Open+Sans:wght@400;600;800&display=swap">
<style>
  :root {
    --brand-blue: #1b4a9e;
    --sky-blue: #3ec4f0;
    --ink: #1a1a1a;
    --paper: #ffffff;
    --backdrop: #e9ebef;
  }
  * { margin: 0; padding: 0; box-sizing: border-box; }
  html, body { width: 1200px; height: 1200px; overflow: hidden; }
  body {
    background: var(--backdrop);
    font-family: "Arimo", Arial, sans-serif;
    position: relative;
  }
  .card {
    position: absolute;
    top: 200px;
    width: 440px;
    height: 770px;
    border-radius: 28px;
    box-shadow: 0 10px 30px rgba(0,0,0,0.12);
    overflow: hidden;
  }
  .card-front { left: 120px; background: var(--paper); }
  .card-back { left: 640px; background: var(--brand-blue); }

  /* front */
  .brand-lockup {
    position: absolute;
    top: 120px; left: 0; right: 0;
    display: flex; align-items: center; justify-content: center; gap: 18px;
  }
  .brand-name {
    font-family: "Open Sans", sans-serif;
    font-weight: 800;
    font-size: 34px;
    line-height: 1.05;
    color: var(--brand-blue);
    width: 200px;
  }
  .brand-dot {
    width: 90px; height: 90px; border-radius: 50%;
    background: var(--sky-blue);
    flex: none;
  }
  .motto {
    position: absolute;
    top: 262px; left: 0; right: 0;
    text-align: center;
    font-family: "Open Sans", sans-serif;
    font-size: 15px;
    letter-spacing: 1px;
    color: var(--ink);
  }
  .person {
    position: absolute; top: 390px; left: 0; right: 0; text-align: center;
  }
  .person-name {
    font-weight: 700; font-size: 38px; letter-spacing: 0.5px;
    color: var(--brand-blue);
  }
  .person-name .surname { color: var(--sky-blue); }
  .person-role { font-size: 20px; color: var(--ink); margin-top: 2px; }

  .contact-divider {
    position: absolute; top: 498px; left: 40px; right: 40px;
    display: flex; align-items: center; gap: 10px;
  }
  .contact-divider .rule { flex: 1; height: 1px; background: var(--sky-blue); }
  .contact-icons { display: flex; gap: 8px; }
  .contact-icons svg { width: 30px; height: 30px; display: block; }

  .contact-list {
    position: absolute; top: 534px; left: 0; right: 0;
    text-align: center; list-style: none;
    font-size: 20px; line-height: 1.45; color: var(--ink);
  }
  .address-rule {
    position: absolute; top: 668px; left: 40px; right: 40px;
    height: 1px; background: var(--sky-blue);
  }
  .address {
    position: absolute; top: 686px; left: 0; right: 0;
    text-align: center; font-style: normal;
    font-size: 20px; line-height: 1.4; color: var(--ink);
  }

  /* back */
  .back-lockup {
    position: absolute;
    left: 50%; top: 50%;
    width: 620px;
    transform: translate(-50%, -50%) rotate(-90deg);
    display: flex; align-items: center; justify-content: center; gap: 24px;
  }
  .back-text { display: flex; flex-direction: column; }
  .back-name {
    font-family: "Open Sans", sans-serif;
    font-weight: 800; font-size: 50px; line-height: 1.05;
    color: var(--paper);
  }
  .back-motto {
    font-family: "Open Sans", sans-serif;
    font-size: 18px; letter-spacing: 1.5px; margin-top: 14px;
    color: var(--paper);
  }
  .back-dot {
    width: 150px; height: 150px; border-radius: 50%;
    background: var(--paper); flex: none;
  }
</style>
</head>
<body>

<section class="card card-front">
  <div class="brand-lockup">
    <div class="brand-name">Harmony Swift Care</div>
    <div class="brand-dot"></div>
  </div>
  <p class="motto">FAST | RELIABLE | CONVENIENT</p>

  <div class="person">
    <h1 class="person-name">ELENA <span class="surname">MARSH</span></h1>
    <p class="person-role">CEO/Founder</p>
  </div>

  <div class="contact-divider">
    <span class="rule"></span>
    <div class="contact-icons">
      <svg viewBox="0 0 30 30" aria-label="Office phone"><rect width="30" height="30" rx="5" fill="var(--brand-blue)"/><path d="M10 8c1-1 2 0 3 2s0 2-1 3c1 2 3 4 5 5 1-1 1-2 3-1s3 2 2 3c-2 3-6 2-9-1s-5-8-3-11z" fill="#fff"/></svg>
      <svg viewBox="0 0 30 30" aria-label="Mobile"><rect width="30" height="30" rx="5" fill="var(--brand-blue)"/><rect x="10" y="6" width="10" height="18" rx="2" fill="none" stroke="#fff" stroke-width="2"/><circle cx="15" cy="21" r="1" fill="#fff"/></svg>
      <svg viewBox="0 0 30 30" aria-label="Email"><rect width="30" height="30" rx="5" fill="var(--brand-blue)"/><rect x="7" y="9" width="16" height="12" fill="none" stroke="#fff" stroke-width="2"/><path d="M7 9l8 7 8-7" fill="none" stroke="#fff" stroke-width="2"/></svg>
      <svg viewBox="0 0 30 30" aria-label="Website"><rect width="30" height="30" rx="5" fill="var(--brand-blue)"/><circle cx="15" cy="15" r="8" fill="none" stroke="#fff" stroke-width="2"/><path d="M7 15h16M15 7c-4 5-4 11 0 16M15 7c4 5 4 11 0 16" fill="none" stroke="#fff" stroke-width="1.5"/></svg>
    </div>
    <span class="rule"></span>
  </div>

  <ul class="contact-list">
    <li>+1 (555) 014-2276</li>
    <li>+1 (555) 019-3381</li>
    <li>info@swiftcarehub.example</li>
    <li>www.swiftcarehub.example</li>
  </ul>

  <div class="address-rule"></div>
  <address class="address">P.O. Box 42 Elmridge CD<br>Country Name 3190</address>
</section>

<section class="card card-back">
  <div class="back-lockup">
    <div class="back-text">
      <div class="back-name">Harmony Swift Care</div>
      <div class="back-motto">FAST | RELIABLE | CONVENIENT</div>
    </div>
    <div class="back-dot"></div>
  </div>
</section>

</body>
</html>
```